Postcard Design

Law office.
Details are on the attached pdf file:
NOTE: the following items are to be changed, as follows:
1. price is 799
2. delete "Expires 2-8-13"
3. make "Nevada County's..." into "Northern California's ... "
4. Someplace where it fits nicely, add "Fast, Easy, Done!"
5. Delete "no obligation first visit"
6. That attached pdf was a successful ad so I want to maintain that look GENERALLY, but I'm not stuck on anything in particular. Some freedom to play with it for a perfect ad.
7. I'll attach the revised picture and the logo.

```html
<!DOCTYPE html>
<html lang="en">
<head>
<meta charset="utf-8">
<title>Law Office of Daniel R. Moreno – Estate Plans Postcard</title>
<link rel="stylesheet" href="https://fonts.googleapis.com/css2?family=Cormorant+Garamond:wght@500;600;700&family=Crimson+Text:ital,wght@0,400;0,600;0,700;1,400&display=swap">
<style>
  :root {
    --page-bg: #e9e3d8;
    --card-white: #ffffff;
    --frame-dark: #1a1714;
    --frame-gold: #c9a96a;
    --ink: #151311;
    --ink-soft: #3a3632;
    --panel-light: rgba(245, 245, 247, 0.9);
    --scene-dark: #3b3330;
    --scene-warm: #8c6a4e;
    --scene-cream: #d9cbb6;
    --portrait-top: #7d6656;
    --portrait-bottom: #26242a;
  }
  * { box-sizing: border-box; margin: 0; padding: 0; }
  html, body {
    width: 1200px; height: 900px; overflow: hidden;
    background: var(--page-bg);
    font-family: "Crimson Text", Georgia, serif;
    color: var(--ink);
  }
  .postcard {
    position: absolute; left: 60px; top: 90px;
    width: 1080px; height: 720px;
    background: var(--card-white);
    padding: 14px;
    box-shadow: 0 6px 22px rgba(0,0,0,0.18);
  }
  .postcard__frame {
    position: relative; width: 100%; height: 100%;
    border: 10px solid var(--frame-dark);
    overflow: hidden;
    background: var(--card-white);
  }
  .backdrop-photo {
    position: absolute; inset: 0;
    background: linear-gradient(110deg, var(--scene-dark) 0%, var(--scene-warm) 30%, #b7a99b 55%, #e6e3df 100%);
  }
  .attorney-photo {
    position: absolute; left: 0; top: 0; bottom: 0;
    width: 480px;
    background: linear-gradient(180deg, var(--portrait-top) 0%, #5a4c46 45%, var(--portrait-bottom) 100%);
  }
  .message-panel {
    position: absolute; left: 470px; top: 0; right: 0; bottom: 0;
    background: linear-gradient(90deg, rgba(245,245,247,0.6) 0, var(--panel-light) 10%, var(--panel-light) 100%);
    text-align: center;
    padding-top: 18px;
  }
  .headline { font-weight: 700; font-size: 36px; line-height: 1.05; }
  .subhead { font-style: italic; font-size: 22px; color: var(--ink-soft); margin-top: 4px; }
  .tagline { font-weight: 700; font-size: 34px; margin-top: 22px; }
  .price { font-weight: 700; font-size: 52px; line-height: 1; margin-top: 16px; }
  .price-note { font-size: 18px; }
  .slogan { font-weight: 700; font-size: 56px; line-height: 1.1; margin-top: 16px; }
  .call-line { font-weight: 700; font-size: 27px; margin-top: 10px; }
  .phone {
    display: inline-flex; align-items: center; gap: 12px;
    font-weight: 700; font-size: 40px; margin-top: 4px; letter-spacing: 1px;
  }
  .phone svg { width: 26px; height: 26px; }
  .web-block {
    position: absolute; left: 70px; bottom: 44px; text-align: left;
    font-size: 20px;
  }
  .web-url {
    display: flex; align-items: center; gap: 10px;
    font-weight: 700; font-style: italic; font-size: 22px;
    margin: 8px 0 0 56px;
  }
  .web-url svg { width: 17px; height: 17px; }
  .perk {
    display: flex; align-items: center; gap: 8px;
    font-size: 16px; margin: 14px 0 0 120px;
  }
  .perk::before { content: ""; width: 7px; height: 7px; background: var(--ink); transform: rotate(45deg); }
  .brand-box { position: absolute; right: 22px; bottom: 30px; width: 130px; text-align: center; }
  .brand-box__mark {
    display: flex; flex-direction: column; align-items: center; justify-content: center; gap: 8px;
    width: 104px; height: 104px; margin: 0 auto;
    background: var(--card-white); border: 3px solid var(--frame-dark);
    font-weight: 700; font-size: 20px; line-height: 1;
  }
  .brand-box__mark::before { content: ""; width: 18px; height: 18px; background: var(--ink); }
  .brand-box__note { font-size: 15px; line-height: 1.15; margin-top: 6px; }
  .corner-badge {
    position: absolute; left: 6px; top: 6px;
    width: 40px; height: 40px;
    background: var(--scene-cream); border: 2px solid var(--frame-dark);
  }
  .office-name {
    position: absolute; left: 20px; bottom: 0; width: 520px; height: 128px;
    background: rgba(255,255,255,0.94);
    padding: 14px 0 0 20px;
  }
  .office-name__lead { font-size: 24px; margin-left: 90px; }
  .office-name__name {
    font-family: "Cormorant Garamond", Georgia, serif;
    font-weight: 600; font-size: 64px; line-height: 1;
  }
</style>
</head>
<body>
  <article class="postcard">
    <div class="postcard__frame">
      <div class="backdrop-photo" role="img" aria-label="Soft-focus photo of an office scene with hands signing documents"></div>
      <div class="attorney-photo" role="img" aria-label="Portrait photo of the attorney in a dark suit and tie"></div>
      <span class="corner-badge"></span>

      <section class="message-panel">
        <h1 class="headline">Northern California's<br>Best in Estate Plans</h1>
        <p class="subhead">Living Trusts, Wills &amp; All Necessary Documents</p>
        <p class="tagline">Protect Your Loved Ones!</p>
        <p class="price">$799</p>
        <p class="price-note">Over $2,000 value</p>
        <p class="slogan">Fast, Easy, Done!</p>
        <p class="call-line">It's Easy - Call Now!</p>
        <p class="phone">
          <svg viewBox="0 0 24 24" aria-hidden="true"><path fill="#151311" d="M6.6 10.8a15.1 15.1 0 0 0 6.6 6.6l2.2-2.2c.3-.3.7-.4 1-.2 1.1.4 2.3.6 3.6.6.6 0 1 .4 1 1V20c0 .6-.4 1-1 1C10.6 21 3 13.4 3 4c0-.6.4-1 1-1h3.5c.6 0 1 .4 1 1 0 1.3.2 2.5.6 3.6.1.3 0 .7-.2 1z"/></svg>
          555-0142
        </p>

        <div class="web-block">
          <p>Check me out at :</p>
          <p class="web-url">
            <svg viewBox="0 0 24 24" aria-hidden="true"><circle cx="12" cy="12" r="10" fill="none" stroke="#151311" stroke-width="2"/><path d="M2 12h20M12 2c3 3 3 17 0 20M12 2c-3 3-3 17 0 20" fill="none" stroke="#151311" stroke-width="1.6"/></svg>
            www.DanielMorenoLaw.com
          </p>
          <p class="perk">Free Notarization</p>
        </div>

        <div class="brand-box">
          <div class="brand-box__mark">Moreno<br>Law</div>
          <p class="brand-box__note">Thousands Served<br>Since 1998</p>
        </div>
      </section>

      <div class="office-name">
        <p class="office-name__lead">Law Office Of</p>
        <p class="office-name__name">Daniel R. Moreno</p>
      </div>
    </div>
  </article>
</body>
</html>
```